Volora Laundry and Dry Cleaning Poster

We need a Poster and Window Sticker for our Laundry and Dry cleaning shop (VOLORA LAUNDRY AND DRY CLEANING).
info we like on the design. Logo is included
Company Name: Volora Laundry and Dry Cleaning
Slogan: It Comes Back Clean
Location: Kwentu-Dasor, Accra
Working Hours: Mon-Sat 8am to 5pm
Tel: +233 30 781 6242
email:info@voloralaundry.example
website: www.voloralaundry.example
fb: social.example/voloralaundry

Target Market(s)

Laundry Shop

Colors
33a6d7
9bcb3b

```html
<!DOCTYPE html>
<html lang="en">
<head>
<meta charset="utf-8">
<title>Volora Laundry and Dry Cleaning Poster</title>
<link href="https://fonts.googleapis.com/css2?family=Poppins:wght@500&family=Roboto:wght@700;900&family=Roboto+Condensed:wght@400;700&family=Rubik:wght@400&family=Orbitron:wght@700&display=swap" rel="stylesheet">
<style>
  :root {
    --blue: #1ea3d8;
    --green: #9bcb3b;
    --teal: #15a3a9;
    --band: #13b5a0;
    --white: #ffffff;
    --stage: #e6e8eb;
  }
  * { margin: 0; padding: 0; box-sizing: border-box; }
  html, body {
    width: 1200px; height: 1200px; overflow: hidden;
    background: var(--stage);
  }
  .poster {
    position: absolute; left: 216px; top: 40px;
    width: 823px; height: 1202px;
    transform: scale(0.932); transform-origin: top left;
    background: var(--white);
    box-shadow: 0 10px 30px rgba(0,0,0,0.18);
    overflow: hidden;
  }
  .poster-shapes { position: absolute; inset: 0; width: 823px; height: 1202px; }
  .brand {
    position: absolute; top: 42px; left: 0; width: 100%; height: 137px;
    display: flex; align-items: center; justify-content: center; gap: 18px;
  }
  .brand-dot { width: 96px; height: 96px; border-radius: 50%; background: var(--blue); }
  .brand-name {
    font-family: "Poppins", sans-serif; font-weight: 500;
    font-size: 104px; line-height: 1; color: var(--blue); letter-spacing: -1px;
  }
  .headline {
    position: absolute; left: 0; width: 100%; text-align: center;
    color: var(--blue); font-family: "Roboto", sans-serif; line-height: 1.1;
  }
  .headline-main { top: 720px; font-size: 54px; font-weight: 900; letter-spacing: 3px; }
  .headline-sub { top: 778px; font-size: 32px; font-weight: 700; letter-spacing: 10.5px; padding-left: 10px; }
  .slogan {
    position: absolute; top: 822px; left: 0; width: 100%; text-align: center;
    font-family: "Orbitron", sans-serif; font-weight: 700; font-size: 21px;
    letter-spacing: 8px; color: var(--teal); padding-left: 8px;
  }
  .contact {
    position: absolute; list-style: none;
    font-family: "Rubik", sans-serif; font-size: 18px; letter-spacing: 1.2px; color: var(--teal);
  }
  .contact li { display: flex; align-items: center; height: 35px; white-space: nowrap; }
  .contact svg { width: 22px; height: 22px; margin-right: 14px; flex: none; }
  .contact-left { left: 108px; top: 945px; }
  .contact-right { left: 440px; top: 964px; }
  .contact-right li { height: 33px; }
  .contact-right svg { width: 26px; height: 26px; margin-right: 17px; }
  .hours {
    position: absolute; left: 0; top: 1105px; width: 100%; height: 97px;
    background: var(--band); color: var(--white);
    font-family: "Roboto Condensed", sans-serif; font-size: 25px;
    display: flex; align-items: center;
  }
  .hours-label { font-weight: 700; margin-left: 145px; width: 275px; }
  .hours-time { font-weight: 400; letter-spacing: 1px; }
</style>
</head>
<body>
<div class="poster">
  <svg class="poster-shapes" viewBox="0 0 823 1202">
    <defs>
      <linearGradient id="photoTone" x1="0" y1="0" x2="1" y2="1">
        <stop offset="0" stop-color="#efe6dc"/>
        <stop offset="0.55" stop-color="#ead2cd"/>
        <stop offset="1" stop-color="#d9cfe0"/>
      </linearGradient>
    </defs>
    <rect class="top-band" x="0" y="198" width="823" height="37" fill="#1ea3d8"/>
    <path class="photo" d="M0,260 H823 V587 Q420,710 0,452 Z" fill="url(#photoTone)" role="img" aria-label="Photo: a woman ironing a shirt on an ironing board, seen from above on a light wooden floor"/>
    <path class="swoosh" d="M0,477 Q420,735 823,612 L823,637 Q420,767 0,517 Z" fill="#9bcb3b"/>
  </svg>

  <div class="brand">
    <span class="brand-dot"></span>
    <span class="brand-name">volora</span>
  </div>

  <h1 class="headline headline-main">VOLORA LAUNDRY</h1>
  <h2 class="headline headline-sub">AND DRY CLEANING</h2>
  <p class="slogan">IT COMES BACK CLEAN</p>

  <ul class="contact contact-left">
    <li>
      <svg viewBox="0 0 24 24"><path d="M12 2a7 7 0 0 0-7 7c0 5 7 13 7 13s7-8 7-13a7 7 0 0 0-7-7z" fill="#1ea3d8"/><circle cx="12" cy="9" r="2.8" fill="#fff"/></svg>
      Kwentu-Dasor, Accra
    </li>
    <li>
      <svg viewBox="0 0 24 24"><path d="M6.5 3l3 4-2 2c1 2.5 3 4.5 5.5 5.5l2-2 4 3-1.5 3c-7 0-13-6-13-13z" fill="none" stroke="#1ea3d8" stroke-width="2" stroke-linejoin="round"/></svg>
      +233 30 781 6242
    </li>
    <li>
      <svg viewBox="0 0 24 24"><rect x="2" y="6" width="20" height="13" fill="#1ea3d8"/><path d="M2 6l10 7 10-7" fill="none" stroke="#fff" stroke-width="1.5"/></svg>
      info@voloralaundry.example
    </li>
  </ul>

  <ul class="contact contact-right">
    <li>
      <svg viewBox="0 0 24 24" fill="none" stroke="#1ea3d8" stroke-width="1.6"><circle cx="12" cy="12" r="10"/><ellipse cx="12" cy="12" rx="4.5" ry="10"/><path d="M2 12h20M4 7h16M4 17h16"/></svg>
      www.voloralaundry.example
    </li>
    <li>
      <svg viewBox="0 0 24 24"><circle cx="12" cy="12" r="11" fill="#1ea3d8"/></svg>
      social.example/voloralaundry
    </li>
  </ul>

  <div class="hours">
    <span class="hours-label">WORKING HOURS :</span>
    <span class="hours-time">MON-SAT 8AM TO 5PM</span>
  </div>
</div>
</body>
</html>
```